Corlith Australia Pty Ltd

I require professional business cards with our company logo. We would like something that looks sharp and unique. I have attached the logo for our business, which is an industrial electrical contracting company. But this does not need to be shown on the cards.

Requirements
Must have
• The design must be double sided and needs to have one side with our logo only and the other side with our details.
Should not have
• We do not want any lightening bolts on the designs as this is very common.

```html
<!DOCTYPE html>
<html lang="en">
<head>
<meta charset="utf-8">
<title>Corlith Australia – Business Cards</title>
<link href="https://fonts.googleapis.com/css2?family=Arimo:wght@400;700&display=swap" rel="stylesheet">
<style>
  :root {
    --backdrop: #c9c9c7;
    --card-dark: #1f1c1d;
    --card-mid: #2b2728;
    --gold: #d9b441;
    --gold-light: #f3d77a;
    --gold-deep: #a67f1e;
    --pattern-tone: #262223;
  }
  * { margin: 0; padding: 0; box-sizing: border-box; }
  html, body {
    width: 1200px;
    height: 1023px;
    overflow: hidden;
    background: var(--backdrop);
    font-family: "Arimo", Arial, sans-serif;
  }
  .canvas {
    position: relative;
    width: 1200px;
    height: 1023px;
  }
  .card {
    position: absolute;
    width: 560px;
    height: 320px;
    border-radius: 6px;
    overflow: hidden;
    background: linear-gradient(150deg, var(--card-mid) 0%, var(--card-dark) 60%);
    box-shadow: 0 14px 30px rgba(0,0,0,0.28);
  }
  .card--details { left: 90px; top: 130px; }
  .card--brand { left: 550px; top: 570px; }

  .brand-lockup {
    position: absolute;
    display: flex;
    align-items: center;
    gap: 12px;
    color: var(--gold);
  }
  .brand-dot {
    border: 3px solid var(--gold);
    border-radius: 50%;
    flex: none;
  }
  .brand-name {
    font-weight: 700;
    letter-spacing: 0.12em;
    line-height: 1;
  }
  .brand-sub {
    font-size: 8px;
    letter-spacing: 0.42em;
    margin-top: 4px;
  }

  .card--details .brand-lockup { left: 250px; top: 32px; }
  .card--details .brand-dot { width: 40px; height: 40px; }
  .card--details .brand-name { font-size: 30px; }

  .contact {
    position: absolute;
    right: 34px;
    top: 104px;
    text-align: right;
    color: var(--gold);
    font-size: 15px;
    line-height: 1.35;
    z-index: 2;
  }
  .contact-row { display: flex; justify-content: flex-end; align-items: center; gap: 6px; }
  .contact-tag {
    display: inline-block;
    width: 15px; height: 15px;
    background: var(--gold);
    color: var(--card-dark);
    font-size: 11px;
    font-weight: 700;
    line-height: 15px;
    text-align: center;
  }
  .contact-gap { height: 14px; }

  .person {
    position: absolute;
    left: 34px;
    top: 196px;
    color: var(--gold);
  }
  .person-name { font-size: 24px; }
  .person-role { font-size: 15px; margin-top: 2px; }

  .corner-ring {
    position: absolute;
    left: 100px;
    top: 262px;
    z-index: 1;
  }

  .pattern-field {
    position: absolute;
    inset: 0;
    background: radial-gradient(circle at 50% 45%, #302b2c 0%, var(--pattern-tone) 70%);
  }
  .card--brand .brand-lockup {
    left: 50%; top: 50%;
    transform: translate(-50%, -50%);
  }
  .card--brand .brand-dot { width: 48px; height: 48px; }
  .card--brand .brand-name { font-size: 36px; }
</style>
</head>
<body>
<main class="canvas">

  <section class="card card--details" aria-label="Business card front with contact details">
    <div class="brand-lockup">
      <span class="brand-dot"></span>
      <div>
        <div class="brand-name">CORLITH</div>
        <div class="brand-sub">AUSTRALIA PTY LTD</div>
      </div>
    </div>

    <div class="contact">
      <div class="contact-row"><span class="contact-tag">M</span>0412 903 571</div>
      <div class="contact-row"><span class="contact-tag">P</span>02 4719 6082</div>
      <div class="contact-gap"></div>
      <div>PO Box 318</div>
      <div>Camden Vale NSW 2570</div>
      <div class="contact-gap"></div>
      <div>marcus@corlithaustralia.com.au</div>
      <div>www.corlithaustralia.com.au</div>
    </div>

    <div class="person">
      <div class="person-name">Marcus Reeve</div>
      <div class="person-role">Director</div>
    </div>

    <svg class="corner-ring" width="240" height="58" viewBox="0 0 240 58" aria-hidden="true">
      <circle cx="120" cy="118" r="108" fill="none" stroke="var(--gold)" stroke-width="12"/>
    </svg>
  </section>

  <section class="card card--brand" aria-label="Business card back with company name">
    <div class="pattern-field" role="img" aria-label="Subtle repeating tone-on-tone pattern background"></div>
    <div class="brand-lockup">
      <span class="brand-dot"></span>
      <div class="brand-name">CORLITH</div>
    </div>
  </section>

</main>
</body>
</html>
```